Flyer-Design für Babyfotograf
grinsi77 ist auf alle meine Wünsche eingegangen und hat das Layout sehr gut umgesetzt. Vielen Dank für die gute und reibungslose Zusammenarbeit.
Zielgruppe
Als Fotograf bin ich spezialisiert auf Babybauch- und Neugeborenenshootings, meine Zielgruppe sind daher schwangere Frauen und Familien die bald / vor kurzem Nachwuchs erwartet haben.
Neben den beiden sparten biete ich noch Baby- und Familienshootings an.
Aufgabenstellung
Ich hätte gerne einen besonderen Flyer, ein Faltspiel.
Die Lieferung der fertigen Datei bitte als offene Indesign 5.5 Datei, falls mal Änderungen anstehen und als druckfertige Datei im PDF Format.
Das Datenblatt der Druckerei finden Sie hier:
http://www.kammerl-satz.de/Papierwelt-Laden/PDF-Vorlagen/Vorlage_Endlosfaltkarte_DL.pdf
In der Anlage bekommen Sie einige Infos rund um meine Dienstleistungen, es wäre toll wenn diese textlich ggf. noch besser angepasst werden auf den Kundennutzen und die Vorteile welche der Kunde hat.
Ich hab mal noch einen Flyer beigefügt um mein corporate design zu erkennen.

```html
<!DOCTYPE html>
<html lang="de">
<head>
<meta charset="utf-8">
<title>Faltflyer Babyfotografie</title>
<link href="https://fonts.googleapis.com/css2?family=Lobster&family=Merriweather:ital,wght@0,300;0,400;0,700;1,300&display=swap" rel="stylesheet">
<style>
:root{
  --bg:#474747;
  --red:#9a3328;
  --cream:#e6dfd3;
  --cream-light:#efeae1;
  --text:#4a4a4a;
  --white:#ffffff;
  --guide-pink:#e0457b;
  --guide-cyan:#3fb8e0;
  --band-red:#e3131b;
  --band-orange:#f39200;
}
*{box-sizing:border-box;margin:0;padding:0}
html,body{width:730px;height:1200px;overflow:hidden;background:var(--bg)}
.canvas{position:relative;width:730px;height:1200px}
.script{font-family:'Lobster',cursive;color:var(--red);font-weight:400}
.serif{font-family:'Merriweather',serif}

.large{position:absolute;left:182px}
.thumb{position:absolute;left:11px;width:160px;height:80px;overflow:hidden}
.thumb .panel{transform:scale(0.3008);transform-origin:0 0}
.row-1{top:27px}.row-2{top:320px}.row-3{top:612px}.row-4{top:904px}

.panel{position:relative;width:532px;height:266px;overflow:hidden;background:var(--cream)}
.panel.plain{background:var(--white)}
.photo{position:absolute;box-shadow:0 2px 5px rgba(0,0,0,.35)}

/* Panel 1 – Titel */
.cover-photo{position:absolute;left:0;top:44px;width:356px;height:222px;
  clip-path:polygon(0 5%,100% 0,100% 100%,0 100%);
  background:linear-gradient(160deg,#5d534e 0%,#7d6a5c 35%,#d9b49a 55%,#9c7a55 75%,#6d5a4c 100%)}
.cover-title{position:absolute;left:12px;top:8px;font-size:32px;line-height:1}
.cover-title small{font-size:21px}
.cover-claim{position:absolute;left:371px;top:207px;font-size:22px;line-height:1.25}
.brand-circle{position:absolute;border-radius:50%;background:var(--red);display:flex;align-items:center;justify-content:center}
.brand-name{font-family:'Merriweather',serif;font-weight:300;color:var(--white);font-size:11px;letter-spacing:2.2px;text-align:center}
.circle-1{left:309px;top:22px;width:170px;height:170px}

/* Panel 2 – Einleitung */
.intro-title{position:absolute;left:0;width:532px;top:8px;text-align:center;font-size:22px;line-height:1.28}
.intro-text{position:absolute;left:146px;top:146px;width:241px;height:107px;background:var(--white);padding:12px 10px;
  font-family:'Merriweather',serif;font-weight:300;font-size:7.4px;line-height:1.45;color:var(--text)}
.intro-text p+p{margin-top:4px}
.intro-text strong{font-weight:700}

/* Panel 3 – Gründe */
.reasons{position:absolute;left:133px;top:0;width:266px;height:266px;background:var(--cream)}
.reasons-title{position:absolute;left:0;top:6px;width:266px;text-align:center;font-size:22.5px;line-height:1.25}
.reasons-box{position:absolute;left:6px;top:73px;width:254px;height:189px;display:flex;gap:10px}
.reasons-list{flex:1;background:var(--white);list-style:none;padding:4px 4px 0 6px}
.reasons-list li{display:flex;font-family:'Merriweather',serif;font-weight:300;font-size:5.6px;line-height:1.3;color:var(--text);margin-bottom:3.1px}
.reasons-list .num{font-family:'Lobster',cursive;color:var(--red);font-size:7.4px;width:12px;flex:none;text-align:right;margin-right:4px;line-height:.95}

/* Panel 4 – Rückseite */
.back-feet{position:absolute;left:0;top:118px;width:240px;height:148px;clip-path:polygon(0 9%,100% 0,100% 100%,0 100%);
  background:radial-gradient(ellipse at 55% 55%,#e7b89d 0%,#d7b8a1 35%,#e9dfd0 70%,#f1ebe1 100%)}
.back-baby{position:absolute;left:312px;top:0;width:220px;height:178px;clip-path:polygon(0 0,100% 0,100% 100%,12% 100%);
  background:linear-gradient(160deg,#6b5245 0%,#8a6c5a 40%,#c99b83 55%,#7e8a92 75%,#6b5a4c 100%)}
.circle-4{left:181px;top:48px;width:170px;height:170px}
.contact{position:absolute;left:405px;top:153px;width:122px;height:109px;background:var(--white);padding:10px 8px}
.contact h3{font-family:'Merriweather',serif;font-weight:700;color:var(--red);font-size:8px;line-height:1.35;margin-bottom:6px}
.contact ul{list-style:none}
.contact li{display:flex;gap:4px;font-family:'Merriweather',serif;font-weight:300;font-size:5.6px;line-height:1.35;color:var(--text);margin-bottom:3px}
.contact svg{width:7px;height:7px;flex:none;fill:var(--red);margin-top:.5px}

/* Druckhilfslinien */
.guides{position:absolute;inset:0;pointer-events:none}
.guide-v{position:absolute;top:0;bottom:0;width:0;border-left:.6px solid var(--guide-pink)}
.guide-h{position:absolute;left:0;right:0;height:0;border-top:.6px dashed var(--guide-cyan)}
.band{position:absolute;width:40px;display:flex;align-items:center;justify-content:center;text-align:center;
  font-family:'Merriweather',serif;font-weight:700;font-size:2.6px;line-height:1.3;color:var(--white);padding:2px}
.band.red{background:var(--band-red)}
.band.orange{background:var(--band-orange)}
</style>
</head>
<body>
<main class="canvas">

<!-- Reihe 1: Titelseite -->
<section class="thumb row-1">
  <div class="panel">
    <div class="cover-photo" role="img" aria-label="Schlafendes Neugeborenes in einer alten Holzkiste auf Holzboden"></div>
    <h1 class="cover-title script"><small>Es gibt</small> Momente,</h1>
    <div class="brand-circle circle-1"><span class="brand-name">JONAS BERGER</span></div>
    <p class="cover-claim script">die kommen<br>nie wieder…</p>
  </div>
  <div class="guides">
    <span class="guide-v" style="left:53px"></span><span class="guide-v" style="left:106px"></span>
    <span class="guide-h" style="top:20px"></span><span class="guide-h" style="top:60px"></span>
  </div>
</section>
<section class="large row-1">
  <div class="panel">
    <div class="cover-photo" role="img" aria-label="Schlafendes Neugeborenes in einer alten Holzkiste auf Holzboden"></div>
    <h1 class="cover-title script"><small>Es gibt</small> Momente,</h1>
    <div class="brand-circle circle-1"><span class="brand-name">JONAS BERGER</span></div>
    <p class="cover-claim script">die kommen<br>nie wieder…</p>
  </div>
</section>

<!-- Reihe 2: Innenseite -->
<section class="thumb row-2">
  <div class="panel">
    <div class="photo" style="left:26px;top:7px;width:79px;height:53px;background:linear-gradient(135deg,#e9b9b4,#d9a49c,#8d8a8c)" role="img" aria-label="Hände auf einem Babybauch"></div>
    <div class="photo" style="left:9px;top:75px;width:114px;height:117px;background:linear-gradient(160deg,#8c8a78,#b8b39a 40%,#7e8660 70%,#a4a372)" role="img" aria-label="Schwangere Frau im Park"></div>
    <div class="photo" style="left:26px;top:206px;width:79px;height:53px;background:linear-gradient(135deg,#8a7666,#d9b3a0,#7d6858)" role="img" aria-label="Schlafendes Baby auf Decke"></div>
    <div class="photo" style="left:427px;top:7px;width:79px;height:53px;background:linear-gradient(135deg,#5c4a3f,#9a7c68,#6a5546)" role="img" aria-label="Baby mit Bärenmütze"></div>
    <div class="photo" style="left:410px;top:75px;width:114px;height:117px;background:linear-gradient(180deg,#f4d9a0,#b7a46a 35%,#7f8a4a 60%,#c3b58a)" role="img" aria-label="Werdende Eltern auf einer Wiese"></div>
    <div class="photo" style="left:427px;top:206px;width:79px;height:53px;background:linear-gradient(135deg,#2f2f2f,#9a9a9a,#3c3c3c)" role="img" aria-label="Schwarzweißfoto Mutter mit Baby"></div>
    <div class="photo" style="left:144px;top:68px;width:122px;height:78px;background:linear-gradient(135deg,#f0e6d6,#e2c0aa,#eee3d2)" role="img" aria-label="Neugeborenes auf Fell"></div>
    <div class="photo" style="left:266px;top:66px;width:121px;height:80px;background:linear-gradient(135deg,#2a2a2e,#3a3436 50%,#c9a08a 70%,#2a2a2e)" role="img" aria-label="Schwangere mit Kind vor dunklem Hintergrund"></div>
    <h2 class="intro-title script">… wie die ersten<br>Lebenstage eures Babys!</h2>
    <div class="intro-text">
      <p>Das letzte Drittel der Schwangerschaft, eine spannende Zeit. Der Babybauch wird immer größer, runder und die Freude, Euer Baby in den Händen zu halten wächst jeden Tag.</p>
      <p>Als Fotograf bin ich auf die <strong>Schwangerschaft- und Neugeborenenfotografie</strong> spezialisiert und halte Euch diese so wertvollen Momente für immer fest.</p>
    </div>
  </div>
  <div class="guides">
    <span class="guide-v" style="left:25px"></span><span class="guide-v" style="left:80px"></span><span class="guide-v" style="left:134px"></span>
    <span class="guide-h" style="top:18px"></span><span class="guide-h" style="top:62px"></span>
  </div>
</section>
<section class="large row-2">
  <div class="panel">
    <div class="photo" style="left:26px;top:7px;width:79px;height:53px;background:linear-gradient(135deg,#e9b9b4,#d9a49c,#8d8a8c)" role="img" aria-label="Hände auf einem Babybauch"></div>
    <div class="photo" style="left:9px;top:75px;width:114px;height:117px;background:linear-gradient(160deg,#8c8a78,#b8b39a 40%,#7e8660 70%,#a4a372)" role="img" aria-label="Schwangere Frau im Park"></div>
    <div class="photo" style="left:26px;top:206px;width:79px;height:53px;background:linear-gradient(135deg,#8a7666,#d9b3a0,#7d6858)" role="img" aria-label="Schlafendes Baby auf Decke"></div>
    <div class="photo" style="left:427px;top:7px;width:79px;height:53px;background:linear-gradient(135deg,#5c4a3f,#9a7c68,#6a5546)" role="img" aria-label="Baby mit Bärenmütze"></div>
    <div class="photo" style="left:410px;top:75px;width:114px;height:117px;background:linear-gradient(180deg,#f4d9a0,#b7a46a 35%,#7f8a4a 60%,#c3b58a)" role="img" aria-label="Werdende Eltern auf einer Wiese"></div>
    <div class="photo" style="left:427px;top:206px;width:79px;height:53px;background:linear-gradient(135deg,#2f2f2f,#9a9a9a,#3c3c3c)" role="img" aria-label="Schwarzweißfoto Mutter mit Baby"></div>
    <div class="photo" style="left:144px;top:68px;width:122px;height:78px;background:linear-gradient(135deg,#f0e6d6,#e2c0aa,#eee3d2)" role="img" aria-label="Neugeborenes auf Fell"></div>
    <div class="photo" style="left:266px;top:66px;width:121px;height:80px;background:linear-gradient(135deg,#2a2a2e,#3a3436 50%,#c9a08a 70%,#2a2a2e)" role="img" aria-label="Schwangere mit Kind vor dunklem Hintergrund"></div>
    <h2 class="intro-title script">… wie die ersten<br>Lebenstage eures Babys!</h2>
    <div class="intro-text">
      <p>Das letzte Drittel der Schwangerschaft, eine spannende Zeit. Der Babybauch wird immer größer, runder und die Freude, Euer Baby in den Händen zu halten wächst jeden Tag.</p>
      <p>Als Fotograf bin ich auf die <strong>Schwangerschaft- und Neugeborenenfotografie</strong> spezialisiert und halte Euch diese so wertvollen Momente für immer fest.</p>
    </div>
  </div>
</section>

<!-- Reihe 3: Gründe -->
<section class="thumb row-3">
  <div class="panel plain">
    <div class="reasons">
      <h2 class="reasons-title script">31 gute Gründe für<br>ein Shooting mit mir…</h2>
    </div>
  </div>
  <div class="guides">
    <div class="band red" style="left:0;top:0;height:20px">Bereich frei lassen</div>
    <div class="band orange" style="left:0;top:20px;height:40px">vom Knick bedeckt</div>
    <div class="band red" style="left:0;top:60px;height:20px">Bereich frei lassen</div>
    <div class="band red" style="left:120px;top:0;height:20px">Bereich frei lassen</div>
    <div class="band orange" style="left:120px;top:20px;height:40px">vom Knick bedeckt</div>
    <div class="band red" style="left:120px;top:60px;height:20px">Bereich frei lassen</div>
    <span class="guide-v" style="left:80px"></span>
    <span class="guide-h" style="top:62px"></span>
  </div>
</section>
<section class="large row-3">
  <div class="panel plain">
    <div class="reasons">
      <h2 class="reasons-title script">31 gute Gründe für<br>ein Shooting mit mir…</h2>
      <div class="reasons-box">
        <ol class="reasons-list">
          <li><span class="num">1</span>Fotos als Datei</li>
          <li><span class="num">2</span>Erfahrung seit 2010</li>
          <li><span class="num">3</span>Parkplatz am Studio</li>
          <li><span class="num">4</span>Spielekiste für die „Großen“</li>
          <li><span class="num">5</span>Sicherheit ist das A&amp;O</li>
          <li><span class="num">6</span>Windeln &amp; Hygieneprodukte</li>
          <li><span class="num">7</span>Kostenloses WLAN</li>
          <li><span class="num">8</span>Große Requisitenauswahl</li>
          <li><span class="num">9</span>Bequeme Fotoauswahl Zuhause</li>
          <li><span class="num">10</span>Gemütlicher Stillbereich</li>
          <li><span class="num">11</span>Babybauchkleider</li>
          <li><span class="num">12</span>Spezialisiert auf Schwangere, Neugeborene, Babys &amp; Familien</li>
          <li><span class="num">13</span>Individuelle Shootings</li>
          <li><span class="num">14</span>Flexible Ortswahl</li>
          <li><span class="num">15</span>Kurze Bearbeitungszeiten</li>
          <li><span class="num">16</span>Sofort verfügbare Bilder</li>
        </ol>
        <ol class="reasons-list">
          <li><span class="num">17</span>Erste-Hilfe</li>
          <li><span class="num">18</span>Autobahnnah</li>
          <li><span class="num">19</span>Regelmäßige Angebote &amp; Aktionen</li>
          <li><span class="num">20</span>Diskretion</li>
          <li><span class="num">21</span>100% Ausführung auch im Krankheitsfall</li>
          <li><span class="num">22</span>Zahlreiche Referenzen</li>
          <li><span class="num">23</span>Geduld &amp; Zeit</li>
          <li><span class="num">24</span>Regelmäßig neue Fotos (Babypass)</li>
          <li><span class="num">25</span>Abendshooting</li>
          <li><span class="num">26</span>Zufriedenheit</li>
          <li><span class="num">27</span>Empfehlungen bei zB Wandbildern</li>
          <li><span class="num">28</span>Auf dem neuesten Stand</li>
          <li><span class="num">29</span>EC Zahlung</li>
          <li><span class="num">30</span>Hochwertige Produkte</li>
          <li><span class="num">31</span>Kostenfreie Getränke</li>
        </ol>
      </div>
    </div>
  </div>
</section>

<!-- Reihe 4: Rückseite -->
<section class="thumb row-4">
  <div class="panel">
    <div class="back-feet" role="img" aria-label="Babyfüße auf weicher Wolldecke"></div>
    <div class="back-baby" role="img" aria-label="Schlafendes Neugeborenes in einem Korb mit Tuch"></div>
    <div class="brand-circle circle-4"><span class="brand-name">JONAS BERGER</span></div>
    <div class="contact">
      <h3>Fotostudio<br>Jonas Berger</h3>
      <ul>
        <li><svg viewBox="0 0 10 10"><path d="M5 0a3.5 3.5 0 0 0-3.5 3.5C1.5 6 5 10 5 10s3.5-4 3.5-6.5A3.5 3.5 0 0 0 5 0zm0 5a1.5 1.5 0 1 1 0-3 1.5 1.5 0 0 1 0 3z"/></svg><span>Brunnengasse 12<br>73269 Talheim</span></li>
        <li><svg viewBox="0 0 10 10"><path d="M2 0l2 2.5-1.2 1.3a6 6 0 0 0 3.4 3.4L7.5 6 10 8l-1.3 1.6C4.5 10 0 5.5.4 1.3z"/></svg><span>(0 71 23) 45 67 890</span></li>
        <li><svg viewBox="0 0 10 10"><path d="M0 2h10v6H0zm.8.7L5 5.6l4.2-2.9v-.1H.8z"/></svg><span>jonas@babyfoto-neckartal.de</span></li>
        <li><svg viewBox="0 0 10 10"><path d="M0 1h10v7H6v1h1v1H3V9h1V8H0zm1 1v5h8V2z"/></svg><span>www.babyfoto-neckartal.de</span></li>
        <li><svg viewBox="0 0 10 10"><rect width="10" height="10" rx="1"/></svg><span>babyfoto.neckartal</span></li>
      </ul>
    </div>
  </div>
  <div class="guides">
    <span class="guide-v" style="left:26px"></span><span class="guide-v" style="left:80px"></span><span class="guide-v" style="left:134px"></span>
    <span class="guide-h" style="top:24px"></span><span class="guide-h" style="top:42px"></span>
  </div>
</section>
<section class="large row-4">
  <div class="panel">
    <div class="back-feet" role="img" aria-label="Babyfüße auf weicher Wolldecke"></div>
    <div class="back-baby" role="img" aria-label="Schlafendes Neugeborenes in einem Korb mit Tuch"></div>
    <div class="brand-circle circle-4"><span class="brand-name">JONAS BERGER</span></div>
    <div class="contact">
      <h3>Fotostudio<br>Jonas Berger</h3>
      <ul>
        <li><svg viewBox="0 0 10 10"><path d="M5 0a3.5 3.5 0 0 0-3.5 3.5C1.5 6 5 10 5 10s3.5-4 3.5-6.5A3.5 3.5 0 0 0 5 0zm0 5a1.5 1.5 0 1 1 0-3 1.5 1.5 0 0 1 0 3z"/></svg><span>Brunnengasse 12<br>73269 Talheim</span></li>
        <li><svg viewBox="0 0 10 10"><path d="M2 0l2 2.5-1.2 1.3a6 6 0 0 0 3.4 3.4L7.5 6 10 8l-1.3 1.6C4.5 10 0 5.5.4 1.3z"/></svg><span>(0 71 23) 45 67 890</span></li>
        <li><svg viewBox="0 0 10 10"><path d="M0 2h10v6H0zm.8.7L5 5.6l4.2-2.9v-.1H.8z"/></svg><span>jonas@babyfoto-neckartal.de</span></li>
        <li><svg viewBox="0 0 10 10"><path d="M0 1h10v7H6v1h1v1H3V9h1V8H0zm1 1v5h8V2z"/></svg><span>www.babyfoto-neckartal.de</span></li>
        <li><svg viewBox="0 0 10 10"><rect width="10" height="10" rx="1"/></svg><span>babyfoto.neckartal</span></li>
      </ul>
    </div>
  </div>
</section>

</main>
</body>
</html>
```